new website design for cloud communications company

started building a new site but dont have enough time to finish
http://korbel41.venmatic.com/music-studio-mp

you can also use content from our current website www.vorkamedia.com

would also like to be mobile optimized if possible, and wix compatible

please submit a logo design with website =) project is guaranteed

Industry/Entity Type

Telecommunications

Logo Text

Vorka Media redefining cloud communications

Number of Pages Required

5+ page

Requirements
Must have
• 1.pricing table comparable to this: http://www.bluquemarsh.com/office/plansandpricing.html
• 2. terms of service link
• 3. portals drop down like on the new site with the vorka 2 portal opening inside the site similar to setup on new site shown
• 4. modern look

```html
<!DOCTYPE html>
<html lang="en">
<head>
<meta charset="utf-8">
<title>Vorka Media – Cloud Hosting</title>
<link rel="stylesheet" href="https://fonts.googleapis.com/css2?family=Open+Sans:wght@400;600;700&family=PT+Sans:wght@400;700&family=PT+Sans+Narrow:wght@700&display=swap">
<style>
:root{
  --ink:#444;
  --muted:#777;
  --blue:#2f8ccc;
  --green:#74b43c;
  --orange:#f0622a;
  --bar-dark:#333;
  --nav-dark:#3b3b3b;
  --panel:#555;
  --soft:#f2f2f2;
  --softer:#f7f7f7;
  --line:#dedede;
  --footer:#4a4a4a;
  --band:#666;
  --white:#fff;
}
*{box-sizing:border-box;margin:0;padding:0}
html,body{width:1200px;height:2338px;overflow:hidden}
body{font-family:"Open Sans",Arial,sans-serif;color:var(--ink);background:var(--white);position:relative}
.wrap{width:900px;margin:0 auto;position:relative;height:100%}
.band{position:absolute;left:0;width:1200px}

/* top bar */
.topbar{top:0;height:45px;background:var(--bar-dark);border-bottom:1px solid #2a2a2a}
.topbar .phone{position:absolute;left:0;top:13px;color:#ccc;font-size:14px;display:flex;align-items:center;gap:10px;white-space:nowrap}
.topbar .actions{position:absolute;right:0;top:10px;display:flex;gap:8px}
.btn-small{height:26px;padding:0 14px;font-size:10px;font-weight:700;color:#fff;display:flex;align-items:center;justify-content:center;gap:8px;border-radius:2px;white-space:nowrap}
.btn-login{background:#5a5a5a;width:70px}
.btn-chat{background:var(--green);width:102px}

/* nav */
.navbar{top:45px;height:80px;background:var(--nav-dark)}
.logo{position:absolute;left:0;top:20px;display:flex;align-items:center;gap:8px}
.logo .mark{width:14px;height:14px;background:var(--blue);border-radius:50%}
.logo .name{font-family:"PT Sans",sans-serif;font-weight:700;font-size:28px;color:var(--blue);line-height:1;white-space:nowrap}
.logo .tag{position:absolute;left:22px;top:32px;font-size:8px;color:#ccc;white-space:nowrap}
.menu{position:absolute;left:232px;top:0;height:80px;display:flex;list-style:none}
.menu li{height:80px;display:flex;align-items:center;padding:0 16px;font-size:11px;color:#ccc;text-transform:uppercase;white-space:nowrap}
.menu li.active{background:#333;color:#fff;border-top:3px solid var(--blue)}

/* hero */
.hero{top:125px;height:473px;background:linear-gradient(180deg,#1c1c1c 0%,#2e2e2e 45%,#1a1a1a 100%);text-align:center;color:#fff;overflow:hidden}
.hero-photo{position:absolute;inset:0;background:radial-gradient(ellipse at 50% 40%,#4a4a4a 0%,#2a2a2a 45%,#151515 100%)}
.hero .kicker{position:absolute;top:160px;width:100%;font-family:"PT Sans Narrow",sans-serif;font-size:22px;font-weight:700;letter-spacing:.3px;line-height:1.1}
.hero h1{position:absolute;top:180px;width:100%;font-family:"PT Sans Narrow",sans-serif;font-size:64px;font-weight:700;letter-spacing:-.5px;line-height:1.1}
.hero .offer{position:absolute;top:243px;width:100%;font-family:"PT Sans",sans-serif;font-size:17px;white-space:nowrap}
.hero .offer em{font-style:normal;color:var(--green)}
.hero .cta{position:absolute;top:288px;left:466px;width:220px;height:33px;background:var(--orange);border-radius:3px;font-size:13px;font-weight:700;line-height:33px;text-transform:uppercase}
.server-unit{position:absolute;left:250px;top:350px;width:685px;height:123px;background:linear-gradient(180deg,#5a5a5a 0%,#2b2b2b 35%,#1b1b1b 100%);border-radius:6px 6px 0 0}

/* domain */
.domain{top:598px;height:64px;background:var(--soft)}
.domain-box{position:absolute;left:0;top:6px;width:900px;height:50px;background:#fff;box-shadow:0 1px 3px rgba(0,0,0,.15);display:flex;align-items:center;padding:0 10px 0 20px;gap:8px}
.domain-box label{font-size:11px;font-weight:700;color:#555;width:165px;white-space:nowrap}
.domain-box .field{width:358px;height:33px;border:1px solid #ddd;font-size:11px;color:#aaa;padding:9px 8px}
.btn-block{height:33px;font-size:11px;font-weight:700;color:#fff;display:flex;align-items:center;justify-content:center;text-transform:uppercase;white-space:nowrap}
.btn-check{width:152px;background:var(--green)}
.btn-order{width:162px;background:var(--panel);border:2px solid #ddd}

/* welcome */
.welcome{top:662px;height:295px;background:var(--soft)}
.welcome h2{position:absolute;top:26px;left:0;font-weight:400;font-size:24px;color:var(--blue)}
.welcome .photo{position:absolute;left:1px;top:75px;width:193px;height:168px;border:4px solid #fff;box-shadow:0 0 2px rgba(0,0,0,.2);background:linear-gradient(180deg,#5e95d4 0%,#9fc4e8 55%,#6aa63e 62%,#4d8a2c 100%)}
.welcome .intro{position:absolute;left:219px;top:72px;width:420px;font-size:11.5px;line-height:1.55;color:#555}
.checklist{position:absolute;left:219px;top:142px;width:420px;display:grid;grid-template-columns:204px 216px;row-gap:11px;list-style:none;font-size:11px;color:#555}
.checklist li{display:flex;align-items:center;gap:9px;white-space:nowrap}
.quote{position:absolute;left:671px;top:72px;width:229px;height:149px;background:#fff;padding:18px 20px;box-shadow:0 1px 2px rgba(0,0,0,.08)}
.quote h3{font-family:"PT Sans",sans-serif;font-size:16px;color:#333;display:flex;gap:10px}
.quote h3 span{color:#ccc}
.quote p{margin-top:16px;font-size:11px;line-height:1.6;color:#666}
.quote::after{content:"";position:absolute;left:40px;bottom:-16px;border-right:18px solid transparent;border-top:16px solid #fff}
.quote-by{position:absolute;left:720px;top:236px;font-size:10px;color:#999;line-height:1.5}
.quote-by span{color:var(--blue)}

/* features */
.features{top:957px;height:349px;background:var(--softer);border-top:1px solid #e4e4e4;border-bottom:1px solid #e4e4e4}
.feature{position:absolute;top:40px;width:290px;text-align:center}
.feature svg{display:block;margin:0 auto}
.feature h3{margin-top:32px;font-family:"PT Sans",sans-serif;font-weight:400;font-size:20px;color:#333}
.feature h3 span{color:var(--blue)}
.feature p{margin:8px auto 0;width:265px;font-size:10.5px;line-height:1.5;color:#666}

/* pricing */
.pricing{top:1306px;height:434px;background:#fff}
.plan{position:absolute;top:39px;width:213px;height:356px;text-align:center}
.plan svg.frame{position:absolute;left:0;top:0}
.plan-title{position:relative;height:45px;background:var(--nav-dark);color:#fff;font-family:"PT Sans",sans-serif;font-size:21px;line-height:45px}
.plan.featured .plan-title{background:var(--green)}
.plan .price{position:relative;height:54px;padding-top:10px;font-family:"PT Sans",sans-serif;font-weight:700;font-size:20px;color:#222;line-height:1}
.plan .price small{display:block;font-family:"Open Sans",sans-serif;font-weight:400;font-size:8px;color:#555;margin-top:1px}
.plan ul{position:relative;list-style:none}
.plan li{height:36px;border-top:1px solid #e6e6e6;font-size:11px;color:#555;display:flex;align-items:center;justify-content:center;margin:0 1px;white-space:nowrap}
.plan .signup{position:relative;border-top:1px solid #e6e6e6;margin:0 1px;padding-top:13px}
.plan .signup span{display:inline-block;width:100px;height:27px;line-height:27px;background:var(--panel);color:#fff;font-size:11px;font-weight:700;border-radius:2px}
.plan.featured .signup span{background:#2a8fd6}

/* partners */
.partners{top:1740px;height:98px;background:#ededed}
.partner-row{position:absolute;left:0;top:30px;width:900px;display:flex;justify-content:space-between;align-items:center}
.partner-row span{font-family:"PT Sans",sans-serif;font-weight:700;font-size:26px;color:#a9a9a9;display:flex;align-items:center;gap:8px}
.partner-row i{display:inline-block;width:18px;height:18px;background:#b5b5b5}
.skyline{top:1838px;height:94px;background:linear-gradient(180deg,#ededed 0%,#c9c9c9 45%,#777 85%,#666 100%)}

/* blog band */
.blog{top:1932px;height:118px;background:var(--band)}
.blog .thumb{position:absolute;left:1px;top:26px;width:67px;height:61px;border:3px solid #fff;background:linear-gradient(180deg,#8dbbe4 0%,#bcd9ef 45%,#7fb04a 60%,#5b8f2f 100%)}
.blog .meta{position:absolute;left:82px;top:24px;width:520px;color:#fff}
.blog .meta h4{font-family:"PT Sans",sans-serif;font-size:14px;text-transform:uppercase}
.blog .meta h4 span{font-family:"Open Sans",sans-serif;font-size:10px;font-weight:400;color:var(--blue);text-transform:none;font-style:italic;margin-left:4px}
.blog .meta h5{font-family:"PT Sans",sans-serif;font-weight:400;font-size:15px;margin-top:3px}
.blog .meta p{font-size:10px;line-height:1.5;margin-top:3px}
.blog .meta p span{color:var(--blue)}
.subscribe{position:absolute;left:623px;top:36px;width:277px;height:59px;background:#555;padding:13px 14px;display:flex}
.subscribe .field{width:186px;height:32px;background:#fff;font-size:11px;color:#888;padding:9px 8px}
.subscribe .go{width:63px;height:32px;background:#1e8fd5;color:#fff;font-size:11px;font-weight:700;line-height:32px;text-align:center}

/* footer */
.site-footer{top:2050px;height:253px;background:var(--footer);border-top:1px solid #5a5a5a}
.cols{position:absolute;left:0;top:62px;display:flex}
.col{width:182px}
.col h4{font-family:"PT Sans",sans-serif;font-size:15px;color:#fff;margin-bottom:14px;white-space:nowrap}
.col ul{list-style:none}
.col li{font-size:11px;color:#eee;height:26.5px;display:flex;align-items:center;gap:10px;white-space:nowrap}
.col .sq{width:18px;height:18px;border-radius:2px}
.cards{display:flex;gap:4px;margin-top:6px;padding-left:0}
.cards i{width:28px;height:18px;border-radius:2px;background:#e8e8e8}
.copyright{top:2303px;height:35px;background:var(--bar-dark);font-size:10px;color:#bbb}
.copyright .wrap{display:flex;justify-content:space-between;align-items:center}
.copyright a{color:#ddd;text-decoration:none}
</style>
</head>
<body>

<header class="band topbar">
  <div class="wrap">
    <div class="phone">
      <svg width="10" height="15" viewBox="0 0 10 15"><rect x="0.75" y="0.75" width="8.5" height="13.5" rx="1.5" fill="none" stroke="#ccc" stroke-width="1.5"/><circle cx="5" cy="11.8" r="0.9" fill="#ccc"/></svg>
      (+1) 555 014 2290
    </div>
    <div class="actions">
      <div class="btn-small btn-login">
        <svg width="8" height="10" viewBox="0 0 8 10"><rect x="0" y="4" width="8" height="6" fill="#fff"/><path d="M2 4V2.5a2 2 0 0 1 4 0V4" fill="none" stroke="#fff" stroke-width="1.3"/></svg>LOGIN</div>
      <div class="btn-small btn-chat">
        <svg width="10" height="10" viewBox="0 0 10 10"><circle cx="5" cy="3" r="2.5" fill="#fff"/><path d="M0 10a5 4 0 0 1 10 0z" fill="#fff"/></svg>LIVE CHAT</div>
    </div>
  </div>
</header>

<nav class="band navbar">
  <div class="wrap">
    <div class="logo">
      <span class="mark"></span>
      <span class="name">Vorka Media</span>
      <span class="tag">redefining cloud communications</span>
    </div>
    <ul class="menu">
      <li class="active">Home</li>
      <li>About Us</li>
      <li>Web Hosting</li>
      <li>Dedicated Servers</li>
      <li>Cloud Servers</li>
      <li>Contact Us</li>
    </ul>
  </div>
</nav>

<section class="band hero">
  <div class="hero-photo" role="img" aria-label="Dim server room with rows of rack cabinets"></div>
  <p class="kicker">RELIABLE AND TRUSTED HOSTING QUALITY SERVER AND</p>
  <h1>FASTEST CONNECTION</h1>
  <p class="offer">No Setup Fees and<em>30 Days</em> Money Back Guarantee 3 Months Free on Every Shared Account</p>
  <div class="cta">See All Dedicated Server</div>
  <div class="server-unit" role="img" aria-label="Front of a rack-mounted server unit"></div>
</section>

<section class="band domain">
  <div class="wrap">
    <div class="domain-box">
      <label>CHECK YOUR DOMAIN NAME :</label>
      <div class="field">yourdomain.com</div>
      <div class="btn-block btn-check">Check Availability</div>
      <div class="btn-block btn-order">Order Hosting Only</div>
    </div>
  </div>
</section>

<section class="band welcome">
  <div class="wrap">
    <h2>Welcome to Nimbla Host</h2>
    <div class="photo" role="img" aria-label="Child sitting on grass with a laptop under a blue sky"></div>
    <p class="intro">Lorem ipsum dolor sit amet, consectetur adipisicing elit, sed do eiusmod tempor incididunt ut labore et dolore magna aliqua. Ut enim ad minim veniam, quis nostrud exercitation ullamco laboris.</p>
    <ul class="checklist">
      <li><svg width="10" height="8" viewBox="0 0 10 8"><path d="M1 4l3 3 5-6" fill="none" stroke="#333" stroke-width="2"/></svg>Shared Hosting</li>
      <li><svg width="10" height="8" viewBox="0 0 10 8"><path d="M1 4l3 3 5-6" fill="none" stroke="#333" stroke-width="2"/></svg>VPS</li>
      <li><svg width="10" height="8" viewBox="0 0 10 8"><path d="M1 4l3 3 5-6" fill="none" stroke="#333" stroke-width="2"/></svg>Shared Cloud Hosting</li>
      <li><svg width="10" height="8" viewBox="0 0 10 8"><path d="M1 4l3 3 5-6" fill="none" stroke="#333" stroke-width="2"/></svg>Cloud VPS +Reseller Hosting</li>
      <li><svg width="10" height="8" viewBox="0 0 10 8"><path d="M1 4l3 3 5-6" fill="none" stroke="#333" stroke-width="2"/></svg>Reseller + Shared Hosting</li>
      <li><svg width="10" height="8" viewBox="0 0 10 8"><path d="M1 4l3 3 5-6" fill="none" stroke="#333" stroke-width="2"/></svg>Reseller Cloude Hosting</li>
      <li><svg width="10" height="8" viewBox="0 0 10 8"><path d="M1 4l3 3 5-6" fill="none" stroke="#333" stroke-width="2"/></svg>Reseller Cloude Hosting</li>
      <li><svg width="10" height="8" viewBox="0 0 10 8"><path d="M1 4l3 3 5-6" fill="none" stroke="#333" stroke-width="2"/></svg>Cloude Hosting + Cloud VPS</li>
    </ul>
    <div class="quote">
      <h3><span>“</span>Happy Clients</h3>
      <p>Nimbla Host ipsum dolor sit amet, that the adipisicing elit, sed do eiusmod that tempor incididunt ut labore et are dolore magna aliqua.</p>
    </div>
    <div class="quote-by">Lena Ortiz,<br><span>CEO Nimbla Host</span></div>
  </div>
</section>

<section class="band features">
  <div class="wrap">
    <div class="feature" style="left:-13px">
      <svg width="163" height="172" viewBox="0 0 163 172"><polygon points="81.5,2 161,45 161,127 81.5,170 2,127 2,45" fill="#ededed" stroke="#fff" stroke-width="3"/><polygon points="81.5,14 150,51 150,121 81.5,158 13,121 13,51" fill="#e2e2e2"/><g stroke="#333" stroke-width="5" stroke-linecap="round"><path d="M68 100l28-28"/><path d="M68 72l26 26"/></g><circle cx="66" cy="70" r="7" fill="none" stroke="#333" stroke-width="3"/></svg>
      <h3><span>System</span> Admin</h3>
      <p>It has survived not only five centuries, but also the leap into electronic typesetting, remaining essentially unchanged. It was popularised.</p>
    </div>
    <div class="feature" style="left:303px">
      <svg width="163" height="172" viewBox="0 0 163 172"><polygon points="81.5,2 161,45 161,127 81.5,170 2,127 2,45" fill="#ededed" stroke="#fff" stroke-width="3"/><polygon points="81.5,14 150,51 150,121 81.5,158 13,121 13,51" fill="#e2e2e2"/><rect x="68" y="68" width="27" height="36" fill="none" stroke="#333" stroke-width="3"/><path d="M68 86h27M77 77h9M77 95h9" stroke="#333" stroke-width="3"/></svg>
      <h3>Backups <span>&amp; Storage</span></h3>
      <p>It has survived not only five centuries, but also the leap into electronic typesetting, remaining essentially unchanged. It was popularised.</p>
    </div>
    <div class="feature" style="left:623px">
      <svg width="163" height="172" viewBox="0 0 163 172"><polygon points="81.5,2 161,45 161,127 81.5,170 2,127 2,45" fill="#ededed" stroke="#fff" stroke-width="3"/><polygon points="81.5,14 150,51 150,121 81.5,158 13,121 13,51" fill="#e2e2e2"/><circle cx="81.5" cy="86" r="19" fill="none" stroke="#333" stroke-width="3"/><path d="M81.5 75v11h8" fill="none" stroke="#333" stroke-width="3"/></svg>
      <h3>24/7 Live <span>Support</span></h3>
      <p>It has survived not only five centuries, but also the leap into electronic typesetting, remaining essentially unchanged. It was popularised.</p>
    </div>
  </div>
</section>

<section class="band pricing">
  <div class="wrap">
    <div class="plan" style="left:0">
      <svg class="frame" width="213" height="356" viewBox="0 0 213 356"><polygon points="0.5,0.5 212.5,0.5 212.5,330 106.5,355 0.5,330" fill="#fff" stroke="#ddd"/></svg>
      <div class="plan-title">Basic</div>
      <div class="price">$15.00<small>per month</small></div>
      <ul><li>50MB Monthly Traffic</li><li>3 Email Account</li><li><svg width="8" height="8" viewBox="0 0 8 8"><path d="M1 1l6 6M7 1l-6 6" stroke="#e0403a" stroke-width="1.8"/></svg></li><li>Theme Updates</li><li>Layered Photoshop Files</li></ul>
      <div class="signup"><span>SIGNUP NOW</span></div>
    </div>
    <div class="plan" style="left:229px">
      <svg class="frame" width="213" height="356" viewBox="0 0 213 356"><polygon points="0.5,0.5 212.5,0.5 212.5,330 106.5,355 0.5,330" fill="#fff" stroke="#ddd"/></svg>
      <div class="plan-title">Standard</div>
      <div class="price">$15.00<small>per month</small></div>
      <ul><li>50MB Monthly Traffic</li><li>3 Email Account</li><li><svg width="10" height="8" viewBox="0 0 10 8"><path d="M1 4l3 3 5-6" fill="none" stroke="#74b43c" stroke-width="2"/></svg></li><li>Theme Updates</li><li>Layered Photoshop Files</li></ul>
      <div class="signup"><span>SIGNUP NOW</span></div>
    </div>
    <div class="plan featured" style="left:458px">
      <svg class="frame" width="213" height="356" viewBox="0 0 213 356"><polygon points="0.5,0.5 212.5,0.5 212.5,330 106.5,355 0.5,330" fill="#fff" stroke="#ddd"/></svg>
      <div class="plan-title">Premium</div>
      <div class="price">$15.00<small>per month</small></div>
      <ul><li>50MB Monthly Traffic</li><li>3 Email Account</li><li><svg width="10" height="8" viewBox="0 0 10 8"><path d="M1 4l3 3 5-6" fill="none" stroke="#74b43c" stroke-width="2"/></svg></li><li>Theme Updates</li><li>Layered Photoshop Files</li></ul>
      <div class="signup"><span>SIGNUP NOW</span></div>
    </div>
    <div class="plan" style="left:687px">
      <svg class="frame" width="213" height="356" viewBox="0 0 213 356"><polygon points="0.5,0.5 212.5,0.5 212.5,330 106.5,355 0.5,330" fill="#fff" stroke="#ddd"/></svg>
      <div class="plan-title">Maximum</div>
      <div class="price">$15.00<small>per month</small></div>
      <ul><li>50MB Monthly Traffic</li><li>3 Email Account</li><li><svg width="10" height="8" viewBox="0 0 10 8"><path d="M1 4l3 3 5-6" fill="none" stroke="#74b43c" stroke-width="2"/></svg></li><li>Theme Updates</li><li>Layered Photoshop Files</li></ul>
      <div class="signup"><span>SIGNUP NOW</span></div>
    </div>
  </div>
</section>

<section class="band partners">
  <div class="wrap">
    <div class="partner-row">
      <span><i></i>Quillon</span>
      <span>Retmo</span>
      <span><i></i>Plainbridge</span>
      <span><i></i></span>
      <span>fernstack</span>
      <span><i></i></span>
    </div>
  </div>
</section>
<section class="band skyline" role="img" aria-label="City skyline silhouette rising into the footer"></section>

<section class="band blog">
  <div class="wrap">
    <div class="thumb" role="img" aria-label="Green field under a blue sky"></div>
    <div class="meta">
      <h4>From our blog<span>Nov 24, 2012</span></h4>
      <h5>Aliquam a mauris tellus a dapibus ipsum...</h5>
      <p>Lorem ipsum dolor sit amet, consectetur adipiscing elit deos vestibulum facilisis enim magnas. Donec rhoncus blandit elementum Pellentesque habitant<span>[...]</span></p>
    </div>
    <div class="subscribe">
      <div class="field">Email Address</div>
      <div class="go">SUBMIT</div>
    </div>
  </div>
</section>

<footer class="band site-footer">
  <div class="wrap">
    <div class="cols">
      <div class="col"><h4>Nimbla Host</h4><ul><li>Home</li><li>About Us</li><li>Cloud Server</li><li>Domain</li><li>Contact Us</li></ul></div>
      <div class="col"><h4>Help &amp; Support</h4><ul><li>FAQ.s</li><li>Live Support</li><li>Support Ticket</li></ul></div>
      <div class="col"><h4>My account</h4><ul><li>Sign In</li><li>View Cart</li><li>My Wishlist</li><li>Track My Order</li><li>Help</li></ul></div>
      <div class="col"><h4>Social Connection</h4><ul>
        <li><i class="sq" style="background:#3b5a98"></i>Socialnet</li>
        <li><i class="sq" style="background:#2fa8e0"></i>View Cart</li>
        <li><i class="sq" style="background:#888"></i>My Wishlist</li>
        <li><i class="sq" style="background:#c4302b"></i>Track My Order</li></ul></div>
      <div class="col"><h4>Get in Touch</h4><ul>
        <li><svg width="9" height="14" viewBox="0 0 9 14"><rect x="0.75" y="0.75" width="7.5" height="12.5" rx="1.3" fill="none" stroke="#fff" stroke-width="1.5"/></svg>(+1) 555 014 2290</li>
        <li><svg width="12" height="9" viewBox="0 0 12 9"><rect x="0.5" y="0.5" width="11" height="8" fill="none" stroke="#fff"/><path d="M0.5 0.5l5.5 4.5 5.5-4.5" fill="none" stroke="#fff"/></svg>info@nimblahost.com</li>
        <li style="height:38px;align-items:flex-start;padding-top:6px"><svg width="10" height="14" viewBox="0 0 10 14"><path d="M5 13.5S.5 8 .5 5a4.5 4.5 0 0 1 9 0c0 3-4.5 8.5-4.5 8.5z" fill="#fff"/><circle cx="5" cy="5" r="1.7" fill="#4a4a4a"/></svg><span>Nimbla Host Ltd, Harbor<br>Row 1258, Eastport</span></li>
      </ul>
        <div class="cards"><i></i><i></i><i></i><i></i><i></i></div>
      </div>
    </div>
  </div>
</footer>

<section class="band copyright">
  <div class="wrap">
    <span>Copyright © 2016 Corvel Studio. All Rights Reserved.</span>
    <span><a href="#">Privacy Policy</a> | <a href="#">Terms &amp; Condition</a></span>
  </div>
</section>

</body>
</html>
```